Business Card Design Project

Create an impressive business care to use
Updates

My logo is available at http://corvalune.example, or

Industry/Entity Type

Business

Requirements
Must have
• company logo

```html
<!DOCTYPE html>
<html lang="en">
<head>
<meta charset="utf-8">
<title>Corvalune Research Corporation – Business Card</title>
<link rel="stylesheet" href="https://fonts.googleapis.com/css2?family=Arimo:wght@400;700&family=Noto+Sans+SC:wght@400&display=swap">
<style>
  :root {
    --backdrop: #2b2b2d;
    --card: #f7f7f5;
    --ink: #1d1d1f;
    --ink-soft: #3a3a3c;
    --green: #6fb33f;
    --blue: #1ea5de;
  }
  * { box-sizing: border-box; margin: 0; padding: 0; }
  html, body {
    width: 1200px; height: 900px; overflow: hidden;
    background: var(--backdrop);
    font-family: "Arimo", Arial, sans-serif;
    color: var(--ink);
  }
  .stage {
    width: 1200px; height: 900px;
    display: flex; align-items: center; justify-content: center;
  }
  .card {
    position: relative;
    width: 900px; height: 514px;
    background: var(--card);
    box-shadow: 0 18px 40px rgba(0,0,0,.45);
  }
  .brand {
    position: absolute; left: 62px; top: 92px;
    display: flex; align-items: center; gap: 14px;
  }
  .brand-dot {
    width: 24px; height: 24px; border-radius: 50%;
    background: var(--green); flex: none;
  }
  .brand-name {
    font-size: 34px; font-weight: 700; line-height: 1.1;
    color: var(--ink);
  }
  .person {
    position: absolute; right: 62px; top: 70px;
    text-align: right; line-height: 1.28;
  }
  .person-name { font-size: 24px; font-weight: 700; }
  .person-name .degree { font-weight: 400; }
  .person-name-zh {
    font-family: "Noto Sans SC", sans-serif;
    font-size: 21px; letter-spacing: 4px; color: var(--ink-soft);
  }
  .person-role { font-size: 22px; font-weight: 700; }
  .contacts {
    position: absolute; left: 62px; bottom: 62px;
    font-size: 17px; color: var(--ink-soft); line-height: 1.55;
  }
  .contacts b { color: var(--ink); }
  .contact-row { display: flex; align-items: center; gap: 8px; white-space: nowrap; }
  .contact-row .sep { width: 10px; }
  .icon { width: 16px; height: 16px; flex: none; }
  .accent-bar {
    width: 560px; height: 9px; margin: 8px 0 10px;
    background: linear-gradient(90deg, var(--green), var(--blue));
  }
  .zh { font-family: "Noto Sans SC", sans-serif; }
</style>
</head>
<body>
<main class="stage">
  <article class="card">
    <header class="brand">
      <span class="brand-dot"></span>
      <div class="brand-name">Corvalune Research Corporation</div>
    </header>

    <section class="person">
      <div class="person-name">MARCUS LIN</div>
      <div class="person-name">TAO, <span class="degree">PhD</span></div>
      <div class="person-name-zh">陶林 博士</div>
      <div class="person-role">CEO</div>
    </section>

    <section class="contacts">
      <div class="contact-row"><b>U.S.:</b> 4820 Lindenfield Ave, Suite 210, Millbrook, CA 90000</div>
      <div class="contact-row">
        <svg class="icon" viewBox="0 0 16 16" aria-hidden="true"><rect x="1" y="3" width="14" height="10" fill="none" stroke="#3a3a3c" stroke-width="1.6"/><path d="M1 3l7 6 7-6" fill="none" stroke="#3a3a3c" stroke-width="1.6"/></svg>
        mtao@corvalune.example
        <span class="sep"></span>
        <svg class="icon" viewBox="0 0 16 16" aria-hidden="true"><rect x="4" y="1" width="8" height="14" rx="1.5" fill="#3a3a3c"/><rect x="5.5" y="3" width="5" height="8" fill="#f7f7f5"/></svg>
        555-014-2273
        <span class="sep"></span>
        <svg class="icon" viewBox="0 0 16 16" aria-hidden="true"><circle cx="8" cy="8" r="6.5" fill="none" stroke="#3a3a3c" stroke-width="1.5"/><ellipse cx="8" cy="8" rx="2.8" ry="6.5" fill="none" stroke="#3a3a3c" stroke-width="1.2"/><path d="M1.5 8h13" stroke="#3a3a3c" stroke-width="1.2"/></svg>
        corvalune.example
      </div>
      <div class="accent-bar"></div>
      <div class="contact-row"><b>CHINA:</b> 318, NO.45 Qinghe Road, Haidian District, Beijing</div>
      <div class="contact-row">
        China 100085 <span class="zh">北京市海淀区清河路45号科技园</span>
        <span class="sep"></span>
        <svg class="icon" viewBox="0 0 16 16" aria-hidden="true"><circle cx="8" cy="8" r="6.5" fill="none" stroke="#3a3a3c" stroke-width="1.5"/><ellipse cx="8" cy="8" rx="2.8" ry="6.5" fill="none" stroke="#3a3a3c" stroke-width="1.2"/><path d="M1.5 8h13" stroke="#3a3a3c" stroke-width="1.2"/></svg>
        lumarin.example
      </div>
    </section>
  </article>
</main>
</body>
</html>
```